Paws Of Kindness Business cards

Design a cool, modern business card for my bully breed rescue.

Contact Information for Business Card

Marlene
517-382-4061 Marlene@PawsOfKindnessRescue.net PawsOfKindnessRescue.net

Font styles to use
Serif
Sans Serif

Colors

Designer to choose colors to be used in the design.

Requirements
Must have
• logo and info. Color
Nice to have
• Foil. Maybe some paw prints on the back or some kind of dog illustration.

```html
<!DOCTYPE html>
<html lang="en">
<head>
<meta charset="utf-8">
<title>Paws Of Kindness – Business Cards</title>
<link rel="stylesheet" href="https://fonts.googleapis.com/css2?family=Michroma&family=Saira:wght@400;500&display=swap">
<style>
  :root {
    --stage: #e4e4e4;
    --card-white: #f7f7f6;
    --ink: #0b0b0b;
    --gold: #f2c80f;
    --red: #e3404b;
    --paper-text: #ffffff;
  }
  * { box-sizing: border-box; margin: 0; padding: 0; }
  html, body {
    width: 1200px; height: 864px; overflow: hidden;
    background: var(--stage);
  }
  .sheet {
    position: relative; width: 1200px; height: 864px;
    display: flex; flex-direction: column; align-items: center; justify-content: center; gap: 30px;
  }
  .card {
    position: relative; width: 680px; height: 388px;
    background: var(--card-white); overflow: hidden;
    box-shadow: 0 6px 18px rgba(0,0,0,0.18);
  }
  .card__art { position: absolute; inset: 0; width: 100%; height: 100%; }
  .brand {
    position: absolute; display: flex; align-items: center; gap: 12px;
  }
  .brand__dot {
    width: 22px; height: 22px; border-radius: 50%; background: var(--ink); flex: none;
  }
  .brand__name {
    font-family: "Michroma", sans-serif; color: var(--ink); white-space: nowrap;
  }
  .card--front .brand { left: 0; right: 0; top: 120px; justify-content: center; }
  .card--front .brand__name { font-size: 30px; }
  .card--back .brand { left: 44px; top: 92px; }
  .card--back .brand__name { font-size: 19px; }
  .card--back .brand__dot { width: 16px; height: 16px; }
  .contact {
    position: absolute; left: 336px; right: 24px; top: 176px; color: var(--paper-text);
  }
  .contact__name {
    font-family: "Michroma", sans-serif; font-size: 30px; font-weight: 400; letter-spacing: 1px; margin-bottom: 26px;
  }
  .contact__list { list-style: none; }
  .contact__item {
    display: flex; align-items: center; gap: 10px;
    font-family: "Saira", sans-serif; font-size: 15px; line-height: 1; margin-bottom: 12px; white-space: nowrap;
  }
  .contact__icon {
    width: 18px; height: 18px; background: var(--gold); flex: none;
    display: flex; align-items: center; justify-content: center;
  }
  .contact__icon svg { width: 12px; height: 12px; }
</style>
</head>
<body>
<main class="sheet">

  <section class="card card--front" aria-label="Card front">
    <svg class="card__art" viewBox="0 0 680 388" preserveAspectRatio="none" aria-hidden="true">
      <path fill="var(--gold)" d="M0,252 C180,262 330,330 480,318 C580,310 640,262 680,236 L680,388 L0,388 Z"/>
      <path fill="var(--card-white)" d="M0,262 C180,272 330,340 480,328 C580,320 640,272 680,246 L680,388 L0,388 Z"/>
      <path fill="var(--ink)" d="M0,268 C180,280 330,350 480,338 C580,330 640,282 680,256 L680,388 L0,388 Z"/>
    </svg>
    <div class="brand">
      <span class="brand__dot"></span>
      <span class="brand__name">Paws Of Kindness</span>
    </div>
  </section>

  <section class="card card--back" aria-label="Card back">
    <svg class="card__art" viewBox="0 0 680 388" preserveAspectRatio="none" aria-hidden="true">
      <path fill="var(--red)" d="M398,0 C360,170 240,300 0,346 L0,388 L680,388 L680,0 Z"/>
      <path fill="var(--card-white)" d="M408,0 C370,172 250,304 0,354 L0,388 L680,388 L680,0 Z"/>
      <path fill="var(--gold)" d="M412,0 C374,174 254,306 0,356 L0,388 L680,388 L680,0 Z"/>
      <path fill="var(--ink)" d="M424,0 C386,178 266,312 0,364 L0,388 L680,388 L680,0 Z"/>
    </svg>
    <div class="brand">
      <span class="brand__dot"></span>
      <span class="brand__name">Paws Of Kindness</span>
    </div>
    <div class="contact">
      <h1 class="contact__name">Marlene</h1>
      <ul class="contact__list">
        <li class="contact__item">
          <span class="contact__icon">
            <svg viewBox="0 0 12 12"><path fill="var(--ink)" d="M2.5,1 L4.5,1 L5.2,3.6 L4,4.6 C4.6,6 6,7.4 7.4,8 L8.4,6.8 L11,7.5 L11,9.5 C11,10.4 10.4,11 9.5,11 C5,11 1,7 1,2.5 C1,1.6 1.6,1 2.5,1 Z"/></svg>
          </span>
          517-382-4061
        </li>
        <li class="contact__item">
          <span class="contact__icon">
            <svg viewBox="0 0 12 12"><rect x="1" y="2.5" width="10" height="7" fill="var(--ink)"/><path d="M1.4,3 L6,6.6 L10.6,3" fill="none" stroke="var(--gold)" stroke-width="1"/></svg>
          </span>
          Marlene@PawsOfKindnessRescue.net
        </li>
        <li class="contact__item">
          <span class="contact__icon">
            <svg viewBox="0 0 12 12"><g fill="none" stroke="var(--ink)" stroke-width="1"><circle cx="6" cy="6" r="4.8"/><ellipse cx="6" cy="6" rx="2" ry="4.8"/><path d="M1.2,6 H10.8 M2,3.6 H10 M2,8.4 H10"/></g></svg>
          </span>
          PawsOfKindnessRescue.net
        </li>
      </ul>
    </div>
  </section>

</main>
</body>
</html>
```